International MultiIndustry Team Coaching Site

Hello Designers,
We need a redesign of the pages attached.
The design must be engaging and modern, with a focus on the user experience, particularly for the "observations" page. Because this is the main page of the website. It is to be used on a 10'' tablet or desktop, to record observations on the fly, so it must be intuitive and efficient.
The positioning of the metrics and observations and etc, are just a reference. you can switch it up if you feel there is a better way (PLEASE DO ;) ).

There are many categories (color coded with borders in the example hpt_6_observations.jpg) and observation metrics within each category. This is the Key page, because it is the One with the most interactions.

The user should know when it has selected a category (there should be some visual hint) and the different metric widgets should be accounted for.
There are 3: The time widget at the end, numerical widgets (recording more or less numbers), and boolean ones (selected or not).

For the numerical widgets, we show plus and minus characters, but you can change this, being creative, keeping in mind that it must work well on a mobile device and desktop, and must be intuitive and quick.

Set your creativity free with the login screen , home screen, categories secret, events screen, journaling and observations screen .

We would like the site/mobile version to have a very modern look. Something that would be found in very popular and user friendly apps.

***** The events, journaling, category and home screens are getting 2 much attention , please focus also on the observations screen *******
Imagine you are a psychologist tasked with observing the behaviour of teenagers during group work. And you have a tablet on which to record what you observe. Now imagine you need to observe during 3 classes: Biology, Math, Physics (these are events). For each class (event) you will have to record observations in 3 categories: Social Interaction, Leadership, Communication (these are categories).
Example of the metrics (these are observations) for Leadership:
" the teenager direct other colleagues" (boolean widget),
"the teenager speaks more than everyone else" (boolean widget)
"the teenager interrupts colleagues speaking" (number widget)
"the work took hh:mm" (time widget)

The observations screen can have any shape and form you think of. It doesn't need to be that single column with yes and nos, or that double column with the squared cards.
thank you.

Hope that was useful intel :)
Available for any questions you might have.
Good luck :)

Target Market(s)

Enterprise teams

Number of Pages Required

5+ page

Font styles to use
Sans Serif

Requirements
Must have
• Modern design

```html
<!DOCTYPE html>
<html lang="en">
<head>
<meta charset="utf-8">
<title>Tandem – Grass Team-3</title>
<link href="https://fonts.googleapis.com/css2?family=Poppins:wght@400;500;600;700&display=swap" rel="stylesheet">
<style>
  :root{
    --bg:#f3f5fa;
    --surface:#ffffff;
    --ink:#2a2f45;
    --muted:#6a7190;
    --line:#e3e6ee;
    --blue:#4d86c4;
    --blue-dark:#3f7ab8;
    --crimson:#c04a72;
    --slate:#6a6e98;
    --violet:#5a4a98;
    --teal:#519fae;
    --teal-dark:#4a98a6;
    --button:#5b4a98;
  }
  *{box-sizing:border-box;margin:0;padding:0}
  html,body{width:1200px;height:696px;overflow:hidden}
  body{
    font-family:"Poppins",sans-serif;
    color:var(--ink);
    background:
      radial-gradient(ellipse 520px 170px at 880px 430px, rgba(200,190,240,.35), transparent 70%),
      radial-gradient(ellipse 600px 200px at 200px 470px, rgba(190,230,220,.25), transparent 70%),
      var(--bg);
    position:relative;
  }
  .app-header{
    height:67px;background:var(--surface);border-bottom:1px solid var(--line);
    display:flex;align-items:center;justify-content:space-between;padding:0 25px;
  }
  .brand{display:flex;align-items:center;gap:8px;font-weight:700;font-size:22px;color:var(--ink)}
  .brand-dot{width:22px;height:22px;border-radius:50%;background:var(--violet)}
  .header-tools{display:flex;align-items:center;gap:22px}
  .theme-toggle{width:38px;height:18px;border-radius:9px;background:var(--blue);position:relative}
  .theme-toggle::after{content:"";position:absolute;right:3px;top:3px;width:12px;height:12px;border-radius:50%;background:#fff}
  .theme-toggle svg{position:absolute;left:5px;top:3px}
  .user{display:flex;align-items:center;gap:12px;font-size:12px;color:var(--muted)}
  .avatar{width:33px;height:33px;border-radius:50%;background:linear-gradient(135deg,#e7e9f0,#c9ccd8);border:1px solid var(--line)}
  main{padding:0 25px}
  .page-head{display:flex;justify-content:space-between;align-items:center;height:77px;margin-top:39px;margin-bottom:-5px}
  .page-title{font-size:20px;font-weight:600;position:relative;top:-11px}
  .back-btn{width:83px;height:38px;border:1px solid var(--blue);border-radius:3px;background:var(--surface);
    display:flex;align-items:center;justify-content:center;gap:10px;color:var(--blue);font-size:13px;font-weight:600;position:relative;top:-11px}
  .welcome-card{background:var(--surface);border-radius:8px;box-shadow:0 2px 10px rgba(40,50,90,.07);
    height:122px;padding:16px 18px 0 18px;margin-top:2px}
  .welcome-line{font-size:13px;color:#4a4f63;display:flex;align-items:baseline;gap:12px}
  .welcome-line strong{color:var(--blue);font-size:15px;font-weight:600}
  .observation-input{margin-top:16px;height:56px;border:1px solid #b9bccb;border-radius:3px;width:100%}
  .categories{display:grid;grid-template-columns:repeat(7,149px);gap:17.5px 17.5px;margin-top:30px}
  .category{height:108px;background:var(--surface);border-radius:2px;padding:10px 12px;box-shadow:0 1px 3px rgba(40,50,90,.04)}
  .category-badge{width:38px;height:38px;border-radius:50%;display:flex;align-items:center;justify-content:center;color:#fff;font-size:22px}
  .category-name{margin-top:9px;font-size:13.5px;line-height:20px;color:var(--muted)}
  .category.is-active{background:var(--teal)}
  .category.is-active .category-badge{background:#fff;color:var(--teal-dark)}
  .category.is-active .category-name{color:#fff}
  .save-row{display:flex;justify-content:center;margin-top:35px}
  .save-btn{width:183px;height:38px;border-radius:3px;background:var(--button);color:#fff;font-size:13px;font-weight:600;
    display:flex;align-items:center;justify-content:center}
</style>
</head>
<body>
<header class="app-header">
  <div class="brand"><span class="brand-dot"></span>Tandem</div>
  <div class="header-tools">
    <div class="theme-toggle">
      <svg width="12" height="12" viewBox="0 0 12 12" fill="none" stroke="#fff" stroke-width="1"><circle cx="6" cy="6" r="2.2"/><path d="M6 .5v1.5M6 10v1.5M.5 6H2M10 6h1.5M2 2l1 1M9 9l1 1M2 10l1-1M9 3l1-1"/></svg>
    </div>
    <div class="user">
      <div class="avatar" role="img" aria-label="User profile photo"></div>
      <span>Owner name</span>
      <svg width="14" height="9" viewBox="0 0 14 9" fill="none" stroke="#4a4f63" stroke-width="1.6"><path d="M1 1.5l6 6 6-6"/></svg>
    </div>
  </div>
</header>
<main>
  <div class="page-head">
    <h1 class="page-title">Grass Team-3</h1>
    <div class="back-btn">
      <svg width="9" height="15" viewBox="0 0 9 15" fill="none" stroke="currentColor" stroke-width="1.5"><path d="M8 1L1.5 7.5 8 14"/></svg>
      Back
    </div>
  </div>
  <section class="welcome-card">
    <p class="welcome-line"><strong>Welcome!</strong>How are you? What are you observing today?</p>
    <div class="observation-input"></div>
  </section>
  <section class="categories">
    <div class="category"><div class="category-badge" style="background:var(--blue)">C</div><p class="category-name">Collaboration</p></div>
    <div class="category"><div class="category-badge" style="background:var(--crimson)">C</div><p class="category-name">Communication</p></div>
    <div class="category"><div class="category-badge" style="background:var(--slate)">O</div><p class="category-name">Openness &amp; Ownership</p></div>
    <div class="category"><div class="category-badge" style="background:var(--violet)">S</div><p class="category-name">Situational Awareness</p></div>
    <div class="category is-active"><div class="category-badge">V</div><p class="category-name">Visualization</p></div>
    <div class="category"><div class="category-badge" style="background:var(--crimson)">L</div><p class="category-name">Limit WIP</p></div>
    <div class="category"><div class="category-badge" style="background:var(--blue)">M</div><p class="category-name">Manage Flow</p></div>
    <div class="category"><div class="category-badge" style="background:var(--teal)">M</div><p class="category-name">Make Policies Explicit</p></div>
  </section>
  <div class="save-row"><div class="save-btn">Save Team Information</div></div>
</main>
</body>
</html>
```